Letterhead Design Project

Professional but modern letterhead.

Target Market(s)

mining companies

Industry/Entity Type

It Professional

Colors

Designer to choose colors to be used in the design.

```html
<!DOCTYPE html>
<html lang="en">
<head>
<meta charset="utf-8">
<title>KORVA Letterhead</title>
<link rel="stylesheet" href="https://fonts.googleapis.com/css2?family=Open+Sans:wght@400;700&display=swap">
<style>
  :root {
    --backdrop: #e4e5e7;
    --paper: #ffffff;
    --ink: #1a1a1a;
    --ink-soft: #2b2b2b;
    --edge-mark: #141414;
    --signature-tone: #d9d9d9;
  }
  * { box-sizing: border-box; margin: 0; padding: 0; }
  html, body {
    width: 1200px; height: 1000px; overflow: hidden;
    background: var(--backdrop);
    font-family: "Open Sans", Arial, sans-serif;
    color: var(--ink);
  }
  .letterhead {
    position: absolute; left: 250px; top: 20px;
    width: 700px; height: 960px;
    background: var(--paper);
    box-shadow: 0 4px 18px rgba(0,0,0,0.12);
  }
  .edge-mark {
    position: absolute; left: 0; width: 7px; background: var(--edge-mark);
  }
  .edge-mark--top { top: 0; height: 110px; }
  .edge-mark--mid { top: 150px; height: 300px; }
  .edge-mark--low { top: 490px; height: 120px; }
  .edge-mark--foot { top: 650px; height: 130px; }
  .brand {
    display: flex; align-items: center; justify-content: center; gap: 12px;
    font-weight: 700; color: var(--ink); letter-spacing: 1px;
  }
  .brand__square { background: var(--ink); display: block; }
  .brand--header { position: absolute; top: 34px; left: 0; right: 0; font-size: 40px; }
  .brand--header .brand__square { width: 44px; height: 44px; }
  .letter {
    position: absolute; left: 64px; top: 130px; width: 580px;
    font-size: 13px; line-height: 17.5px; color: var(--ink-soft);
  }
  .letter__date { margin-bottom: 22px; }
  .letter__recipient { margin-bottom: 22px; }
  .letter__salutation { margin-bottom: 16px; }
  .letter p.body { margin-bottom: 16px; }
  .sign-off { position: absolute; left: 64px; top: 660px; width: 180px; text-align: center; }
  .sign-off__signature { display: block; width: 110px; height: 60px; margin: 0 auto 10px; }
  .sign-off__name { font-weight: 700; font-size: 16px; }
  .sign-off__title { font-size: 15px; }
  .footer { position: absolute; left: 0; right: 0; top: 800px; text-align: center; }
  .brand--footer { font-size: 28px; margin-bottom: 10px; }
  .brand--footer .brand__square { width: 30px; height: 30px; }
  .footer__contact { font-size: 13px; line-height: 16px; color: var(--ink-soft); }
</style>
</head>
<body>
  <main class="letterhead">
    <span class="edge-mark edge-mark--top"></span>
    <span class="edge-mark edge-mark--mid"></span>
    <span class="edge-mark edge-mark--low"></span>
    <span class="edge-mark edge-mark--foot"></span>

    <header class="brand brand--header">
      <span class="brand__square"></span><span class="brand__name">KORVA</span>
    </header>

    <section class="letter">
      <p class="letter__date">16 December 2013</p>
      <p class="letter__recipient">Dr. Helen Marsh<br>Northgate University<br>Medical Center</p>
      <p class="letter__salutation">Dear Dr. Marsh,</p>
      <p class="body">Lorem ipsum dolor sit amet, duo ad audire mediocrem. Cu usu putant perpetua, no vidit assum quaestio pro, oporteat suscipiantur qui an. An vis duis lorem omnes, nec semper probatus te. Pro justo possim forensibus te, pri ne agam omnes.</p>
      <p class="body">Mei verear appetere quaestio ad. Ut his blandit tractatos consequat, eros deleniti ea pri. Ubique facete voluptaria sit at, voluptua postulant assentior qui at. Cu nec appetere reprehendunt, quo cu posse graeco. Urbanitas ullamcorper eum at, nec salutandi definiebas persequeris eu, et ignota petentium eum.</p>
      <p class="body">Graeco diceret consequat duo et, graeci apeirian in nec, brute populo mellore pri te. Eripuit laboramus sadipscing sit ad. Mel consul omnium ea, duis debitis singulis eam ad. Per epicuri volutpat no, ei primis antiopam mea, no omnium equidem eum. Vix dicat eligendi at. No equidem impedit apeirian sed, vel ei esse prodesset, eum dissentiet accommodare ad.</p>
      <p class="body">Sea libris nominati an, prima prompta postulant his ei. Ferri fabellas antiopam eu mei. Id falli expetenda posidonium eos, fabulas expetendis repudiandae pri ne. Sit cu dicant salutatus, et nec equidem impedit tractatos.</p>
      <p class="body">No alia gubergren vix. Nam tollit aliquam sanctus ad, ius no minimum fierent, duo in elitr nostro. Ut pri lorem virtute tincidunt. Et eos nibh maiestatis. Natum harum nominati ei pri.</p>
    </section>

    <div class="sign-off">
      <svg class="sign-off__signature" viewBox="0 0 110 60" role="img" aria-label="Handwritten signature of Daniel Reyes">
        <rect x="0" y="0" width="110" height="60" rx="6" fill="var(--signature-tone)"/>
      </svg>
      <p class="sign-off__name">Daniel Reyes</p>
      <p class="sign-off__title">CEO</p>
    </div>

    <footer class="footer">
      <div class="brand brand--footer">
        <span class="brand__square"></span><span class="brand__name">KORVA</span>
      </div>
      <p class="footer__contact">www.korvadata.com mail@korvadata.com<br>Quarry Road # 48<br>+01 (204) 318-5520. (612) 555-0143.<br>State. Town. Country</p>
    </footer>
  </main>
</body>
</html>
```